We need a design for our security installation based business. Our name is K M Security Systems

We need a business card for a security installation based company. We want to look modern and professional. We would like our company logo used and the three main colours to be white, black and orange. We install intruder alarms, cctv and access control. Our preference would be to use the black/orange design on the front and orange/black on the back. Feel free to post variations.

Target Market(s)

Business owners, commercial property and large residential properties

Industry/Entity Type

Business

Contact Information for Business Card

Owen Pellworth 07812 904 226

Liam Foxcombe 07755 618 042

operations@kmsecuritysystems.example.co.uk

Intruder Alarms
CCTV
Access Control

Colors
f78f20
000000
ffffff

Requirements
Must have
• Must have the logo on the business card somewhere

```html
<!DOCTYPE html>
<html lang="en">
<head>
<meta charset="utf-8">
<title>K M Security Systems – Business Card</title>
<link rel="stylesheet" href="https://fonts.googleapis.com/css2?family=Open+Sans:wght@400;600;700&display=swap">
<style>
  :root {
    --backdrop: #2b2b2b;
    --card: #121212;
    --card-edge: #1c1c1c;
    --orange: #f45d1c;
    --white: #ffffff;
    --divider: #262626;
  }
  * { margin: 0; padding: 0; box-sizing: border-box; }
  html, body {
    width: 1200px;
    height: 900px;
    overflow: hidden;
    background: var(--backdrop);
    font-family: "Open Sans", Arial, sans-serif;
  }
  .stage {
    position: relative;
    width: 1200px;
    height: 900px;
  }
  .card {
    position: absolute;
    top: 300px;
    width: 525px;
    height: 300px;
    background: var(--card);
    border: 1px solid var(--card-edge);
    border-radius: 22px;
    overflow: hidden;
  }
  .card--contact { left: 55px; }
  .card--brand { left: 620px; }

  /* Contact side */
  .brand-block {
    position: absolute;
    left: 0;
    top: 0;
    width: 220px;
    height: 100%;
    display: flex;
    align-items: center;
    justify-content: center;
    gap: 9px;
    border-right: 1px solid var(--divider);
  }
  .brand-mark {
    flex: none;
    width: 13px;
    height: 13px;
    background: var(--orange);
  }
  .brand-name {
    color: var(--orange);
    font-weight: 700;
    font-size: 15.5px;
    letter-spacing: 0.3px;
    white-space: nowrap;
  }
  .contacts {
    position: absolute;
    left: 242px;
    top: 78px;
    right: 18px;
  }
  .person { margin-bottom: 12px; }
  .person-name {
    color: var(--orange);
    font-weight: 600;
    font-size: 18px;
    line-height: 1.2;
  }
  .detail {
    display: flex;
    align-items: center;
    gap: 8px;
    color: var(--white);
    font-size: 13.5px;
    line-height: 1.5;
    white-space: nowrap;
  }
  .detail svg { flex: none; }
  .detail--email { font-size: 11px; margin-top: 6px; gap: 7px; }

  /* Brand side */
  .card--brand {
    display: flex;
    flex-direction: column;
    align-items: center;
    justify-content: center;
    gap: 26px;
  }
  .brand-title {
    display: flex;
    align-items: center;
    gap: 12px;
    color: var(--orange);
    font-weight: 700;
    font-size: 29px;
    letter-spacing: 1px;
    white-space: nowrap;
  }
  .brand-title .brand-mark { width: 18px; height: 18px; }
  .services {
    display: flex;
    align-items: center;
    gap: 12px;
    color: var(--white);
    font-size: 13px;
    font-weight: 600;
  }
  .services .dot {
    width: 8px;
    height: 8px;
    border-radius: 50%;
    background: var(--orange);
  }
</style>
</head>
<body>
<main class="stage">
  <section class="card card--contact">
    <div class="brand-block">
      <span class="brand-mark"></span>
      <span class="brand-name">K M Security Systems</span>
    </div>
    <div class="contacts">
      <div class="person">
        <p class="person-name">Owen Pellworth</p>
        <p class="detail">
          <svg width="10" height="10" viewBox="0 0 24 24" aria-hidden="true"><path fill="#f45d1c" d="M6.6 10.8a15.1 15.1 0 0 0 6.6 6.6l2.2-2.2c.3-.3.7-.4 1-.2 1.1.4 2.3.6 3.6.6.6 0 1 .4 1 1V20c0 .6-.4 1-1 1A17 17 0 0 1 3 4c0-.6.4-1 1-1h3.5c.6 0 1 .4 1 1 0 1.3.2 2.5.6 3.6.1.3 0 .7-.2 1z"/></svg>
          07812 904 226
        </p>
      </div>
      <div class="person">
        <p class="person-name">Liam Foxcombe</p>
        <p class="detail">
          <svg width="10" height="10" viewBox="0 0 24 24" aria-hidden="true"><path fill="#f45d1c" d="M6.6 10.8a15.1 15.1 0 0 0 6.6 6.6l2.2-2.2c.3-.3.7-.4 1-.2 1.1.4 2.3.6 3.6.6.6 0 1 .4 1 1V20c0 .6-.4 1-1 1A17 17 0 0 1 3 4c0-.6.4-1 1-1h3.5c.6 0 1 .4 1 1 0 1.3.2 2.5.6 3.6.1.3 0 .7-.2 1z"/></svg>
          07755 618 042
        </p>
      </div>
      <p class="detail detail--email">
        <svg width="11" height="9" viewBox="0 0 22 16" aria-hidden="true"><rect width="22" height="16" rx="1.5" fill="#f45d1c"/><path d="M1 1l10 8 10-8" fill="none" stroke="#121212" stroke-width="2"/></svg>
        operations@kmsecuritysystems.example.co.uk
      </p>
    </div>
  </section>

  <section class="card card--brand">
    <div class="brand-title">
      <span class="brand-mark"></span>
      <span>K M SECURITY SYSTEMS</span>
    </div>
    <div class="services">
      <span>Intruder Alarms</span>
      <span class="dot"></span>
      <span>CCTV</span>
      <span class="dot"></span>
      <span>Access Control</span>
    </div>
  </section>
</main>
</body>
</html>
```